Texas-Based Roofing Company Looking for Creative Billboard Design

We need a billboard designed for a roofing company in the Dallas - Fort Worth area. They are a tech-forward company that uses drone technology to complete roof inspections. We would like to see a design that is out-of-the-box in terms of creativity. It can be marketed towards a hail/wind storm event, or a creative approach to helping customers think of TANNERLY when it comes to roofing needs.

Target Market(s)

residential homeowners

Industry/Entity Type

Roofing

Requirements
Must have
• Creative approach or play on words to elevate brand awareness.

```html
<!DOCTYPE html>
<html lang="en">
<head>
<meta charset="utf-8">
<title>Tannerly Roofing – Hail Damage Billboard</title>
<link rel="stylesheet" href="https://fonts.googleapis.com/css2?family=Montserrat:wght@300;800&family=Open+Sans:wght@600&display=swap">
<style>
  :root {
    --stage: #d6d6d6;
    --navy: #2b4a73;
    --gold: #e8b43a;
    --ink: #3d3d3d;
    --paper: #ffffff;
    --storm-deep: #1c1330;
    --storm-mid: #4b2f7a;
  }
  * { margin: 0; padding: 0; box-sizing: border-box; }
  html, body { width: 1200px; height: 1200px; overflow: hidden; background: var(--stage); }
  .billboard {
    position: absolute; left: 80px; top: 435px;
    width: 1002px; height: 291px;
    background: var(--paper); overflow: hidden;
  }
  .text-column {
    position: absolute; left: 462px; width: 540px; text-align: center;
  }
  .band-tagline {
    position: absolute; left: 0; right: 0; top: 194px; height: 48px;
    background: var(--gold);
  }
  .tagline {
    top: 0; height: 48px;
    display: flex; flex-direction: column; justify-content: center;
    font-family: "Montserrat", sans-serif; font-weight: 800; font-size: 18.5px;
    line-height: 21px; color: var(--navy);
  }
  .band-web {
    position: absolute; left: 0; right: 0; top: 242px; bottom: 0;
    background: var(--navy);
  }
  .web-line {
    top: 0; height: 49px;
    display: flex; align-items: center; justify-content: center; gap: 14px;
    font-family: "Open Sans", sans-serif; font-weight: 600; font-size: 24.5px;
    color: var(--paper);
  }
  .web-icon { width: 30px; height: 30px; }
  .storm-photo {
    position: absolute; left: 0; top: 0; width: 490px; height: 100%;
    clip-path: polygon(0 0, 483px 0, 385px 100%, 0 100%);
    background:
      radial-gradient(ellipse 60% 30% at 45% 52%, rgba(220,190,255,.55), transparent 70%),
      linear-gradient(180deg, var(--storm-deep) 0%, var(--storm-mid) 45%, #2a1f4a 75%, #120c18 88%, #2a1a10 100%);
  }
  .brand-name {
    top: 58px;
    font-family: "Montserrat", sans-serif; font-weight: 800; font-size: 22px;
    line-height: 28px; color: var(--navy); letter-spacing: 1px;
  }
  .headline {
    top: 100px;
    font-family: "Montserrat", sans-serif; font-weight: normal;
  }
  .headline-lead { font-weight: 300; font-size: 42px; line-height: 46px; color: var(--ink); letter-spacing: 1px; }
  .headline-main { font-weight: 800; font-size: 47.5px; line-height: 46px; color: var(--navy); }
</style>
</head>
<body>
  <section class="billboard">
    <div class="band-tagline">
      <p class="text-column tagline">
        <span>UNSEEN DAMAGE CAN LEAD TO</span>
        <span>WATER DAMAGE AND COSTLY REPAIRS</span>
      </p>
    </div>
    <div class="band-web">
      <div class="text-column web-line">
        <svg class="web-icon" viewBox="0 0 34 34" aria-hidden="true">
          <circle cx="17" cy="17" r="16" fill="var(--gold)"/>
          <g fill="none" stroke="var(--navy)" stroke-width="1.6">
            <circle cx="17" cy="17" r="9"/>
            <ellipse cx="17" cy="17" rx="4" ry="9"/>
            <line x1="8" y1="17" x2="26" y2="17"/>
            <line x1="9.5" y1="12.5" x2="24.5" y2="12.5"/>
            <line x1="9.5" y1="21.5" x2="24.5" y2="21.5"/>
          </g>
        </svg>
        <span>www.tannerlyroofing.com</span>
      </div>
    </div>
    <div class="storm-photo" role="img" aria-label="Night photograph of a purple thunderstorm with many lightning bolts over a lit city skyline"></div>
    <div class="text-column brand-name">TANNERLY ROOFING</div>
    <h1 class="text-column headline">
      <div class="headline-lead">DO NOT IGNORE</div>
      <div class="headline-main">HAIL DAMAGE</div>
    </h1>
  </section>
</body>
</html>
```